New online business - used mobile phones - needs unique eye catching web design that sets it apart

The Handset Bazaar
We are a new business looking for a rapid response for our web site design. We don't want a normal website....... we need to be creative - most important PLEASE view the attached files uploaded 3 March to ensure you get us :)
.
The Handset Bazaar buys new and damaged mobile phones from the public. A simple process they complete to sell their mobile to us; we want our website to reflect this.
Our website needs to be modern, edgy and fun, not corporate and definitely not like any other mobile phone buying site in the world today!!
Our name was taken from a play on the share/stock market which we have tried to bring into the design ....... it hasn't worked with early designs submitted. Now taking a different approach. Refer to new attached files which should help you visualise our concept.

We like layout from Artisan Hive – plvendrake #7318290 design as this is very close to our layout vision.
The first page to tell the public what we do, how we do it, and then they click to accept the instant online quote. (page two they complete details about the mobiles model & condition they are selling, then page three complete their personal details).
Our background preference is dark, blackboard or dark with slight texture
a) We love white on black/dark background either typewriter font or look like hand drawn refer to attached files & quillandfennel.com.au site to see. Would Label font work???

b) Where the light blue colour is on #7318290 this needs to be like chromadex colour classic green, fern green or bright green, not fluorescent lime green or an insipid green.

c) The banner says The Handset Bazaar is open........... for buying mobiles for cash $$$ (we need people to know we BUY used/damaged phones)

d) We love colour either solid colour or looks like it has been coloured in on our dark background. Open to white or pastel background versions refer to attached coffee file.
We like Chromadex Orange 021,Haute Red,Dazzling Blue, Cyan Blue, Beetroot Purple, Island Green.
e) How it works – underneath this title put Our deal …………. It’s easy as…………..quote, post, get paid!!!
Quote – first circle hand drawn icon showing mobile phone & $ sign. Underneath it says .....Obtain Quote for Model & Condition
Post – second circle hand drawn icon show parcel. Underneath it says Free Post
Paid – third circle hand drawn icon showing large $ sign. Underneath it says Payment in Two Days
Plans - is swapped for wording- Get Market Quote with a large button which says GO or CLICK HERE (they click on the button & it takes them to the next page)
f) FAQ
Allow for six FAQ’s we will forward correct content to you for final design layout.

g) About Us
Please allow about a paragraph of text here, we will forward correct content to you for final design layout.
h) Contact Us
At the bottom where normal website have ………. home, contact details, blog, etc, please only put Email us & Call us, then social media icons for FB, Linked In and Twitter

I) LOGO We don’t have one yet, just put The Handset Bazaar at the top & it needs to be large sized font ................we are new and we need to push our name
If you are not clear on our vision ..........please email me and I will reply very quickly.
Thank you for taking the time to read & understand & get us:)

Target Market(s)

20-45 years any body with a spare smart phone that is lying around and they can get cash for. Target market could be slightly older to 50 but focus of 20-40's

Industry/Entity Type

Business

Number of Pages Required

3 page

Font styles to use
Other font styles liked:
• handwritten font or typewriter font

Requirements
Must have
• Read only attached files dated 4 March, tech error with other files, being removed.
• 1 Layout design of Artisan Hive – plvendrake #7318290
• 2 Hand drawn icons - refer to files
• 3 White font needs to look like hand written refer to quillandfennel.com.au or typewriter font - large size font
• 4 Main colours are Black or dark background, green with white text, preference is hand drawn font. The three circles for quote, post & pay with hand drawn icons can be any colour ...... Purple for quote, orange for post & green for paid
• 5 Big green button underneath 3 circles quote/post/pay - customers click on big button to get instant quote
Nice to have
• Coloured in hand drawings as per file
• Great Hand drawings coloured in
Should not have
• NO template designs so it look like you just put some text & a photo. Don't fill the page with mobile phones, one or two is ok, mobile phone pictures date so fast.
• Cartoons

```html
<!DOCTYPE html>
<html lang="en">
<head>
<meta charset="utf-8">
<title>The Handset Bazaar</title>
<link rel="stylesheet" href="https://fonts.googleapis.com/css2?family=Cabin+Sketch:wght@400;700&family=Comic+Neue:wght@700&family=Roboto:wght@300;400&display=swap">
<style>
:root{
  --page:#0b1b4b;
  --header:#071a45;
  --footer:#061334;
  --sky:#1e9be8;
  --faq:#17a3ef;
  --red:#c5262c;
  --orange:#c6601f;
  --white:#ffffff;
  --soft:#d7e6f7;
  --muted:#8fb6dd;
  --social:#1d4f8d;
  --copy:#2b6fb0;
}
*{margin:0;padding:0;box-sizing:border-box}
html,body{width:1200px;height:2375px;overflow:hidden}
body{background:var(--page);color:var(--white);font-family:"Roboto",sans-serif;position:relative}
.sketch{font-family:"Cabin Sketch",cursive}
.comic{font-family:"Comic Neue",cursive;font-weight:700}
.abs{position:absolute}
.center{left:0;width:1200px;text-align:center}

.site-header{position:absolute;top:0;left:0;width:1200px;height:139px;background:var(--header)}
.brand{top:30px;font-family:"Comic Neue",cursive;font-size:56px;font-weight:700;color:var(--sky);letter-spacing:1px}

.hero{position:absolute;top:139px;left:0;width:1200px;height:428px;
  background:radial-gradient(ellipse at 35% 30%,#2a3d6e 0%,#15244c 45%,#0a1330 100%)}
.hero-title{top:84px;font-size:52px;line-height:56px;font-weight:700;letter-spacing:3px;text-transform:uppercase}
.dots{position:absolute;top:307px;left:568px;display:flex;gap:8px}
.dots span{width:12px;height:12px;border-radius:50%;background:var(--white)}
.dots span.on{background:var(--sky)}

.section-title{font-size:40px;font-weight:700;letter-spacing:2px;text-transform:uppercase}
.section-sub{font-size:20px;color:var(--sky);text-transform:uppercase;letter-spacing:1px}

.step{position:absolute;width:300px;text-align:center}
.step-badge{width:146px;height:146px;border-radius:50%;background:var(--red);margin:0 auto;
  box-shadow:0 6px 10px rgba(0,0,0,.45);display:flex;align-items:center;justify-content:center}
.step-name{font-size:33px;font-weight:700;margin-top:8px;letter-spacing:1px}
.step-text{font-size:17px;line-height:26px;color:var(--sky);text-transform:uppercase;margin-top:4px}

.divider{position:absolute;left:285px;width:630px;height:3px;
  background:linear-gradient(90deg,transparent,#061233 30%,#061233 70%,transparent)}

.go-button{position:absolute;left:548px;top:1290px;width:104px;height:104px;border-radius:50%;
  background:var(--orange);box-shadow:0 6px 10px rgba(0,0,0,.45);text-align:center;color:var(--white)}
.go-button span{display:block;font-size:24px;margin-top:2px}

.faq-panel{position:absolute;left:74px;top:1526px;width:1052px;height:405px;background:var(--faq);border-radius:8px}
.faq-item{position:absolute;width:280px;text-align:center}
.faq-q{font-family:"Comic Neue",cursive;font-weight:700;font-size:18px;line-height:23px}
.faq-a{font-size:13px;line-height:21px;color:var(--soft);margin-top:8px;font-weight:300}

.about-text{left:70px;width:1060px;font-size:12.5px;line-height:24px;color:var(--soft);text-align:center;font-weight:300}

.site-footer{position:absolute;top:2251px;left:0;width:1200px;height:124px;background:var(--footer)}
.contact-title{left:74px;top:22px;font-size:14px;letter-spacing:.5px}
.contact-line{left:74px;font-size:12px;display:flex;align-items:center;gap:8px;color:var(--soft)}
.copyright{top:70px;font-size:11px;color:var(--copy)}
.social-link{position:absolute;top:45px;width:32px;height:32px;border-radius:50%;background:var(--social);border:2px solid var(--white)}
</style>
</head>
<body>

<header class="site-header">
  <div class="abs center brand">The Handset Bazaar</div>
</header>

<section class="hero" role="img" aria-label="Background photo of a stock market chart with rising bars and glowing digits">
  <h1 class="abs center hero-title sketch">The Handset Bazaar is<br>open for buying mobiles<br>for cash</h1>
  <div class="dots"><span class="on"></span><span></span><span></span><span></span></div>
</section>

<h2 class="abs center section-title sketch" style="top:617px">How it works</h2>
<p class="abs center section-sub comic" style="top:680px">Our deal …………. It’s easy as…………..quote, post, get paid!!!</p>

<div class="step" style="left:89px;top:730px">
  <div class="step-badge">
    <svg width="80" height="70" viewBox="0 0 80 70" fill="none" stroke="#fff" stroke-width="3" stroke-linejoin="round">
      <rect x="10" y="4" width="28" height="52" rx="4"/>
      <line x1="18" y1="10" x2="30" y2="10"/>
      <rect x="32" y="32" width="40" height="24" rx="2" fill="#c5262c"/>
      <circle cx="52" cy="44" r="7"/>
    </svg>
  </div>
  <div class="step-name sketch">QUOTE</div>
  <div class="step-text comic">Obtain quote for model &amp;<br>condition</div>
</div>

<div class="step" style="left:455px;top:730px">
  <div class="step-badge">
    <svg width="80" height="70" viewBox="0 0 80 70" fill="none" stroke="#fff" stroke-width="3" stroke-linejoin="round">
      <path d="M10 22 L24 10 L70 10 L70 48 L56 60 L10 60 Z" fill="#fff"/>
      <path d="M10 22 L56 22 L56 60 M56 22 L70 10" stroke="#c5262c"/>
    </svg>
  </div>
  <div class="step-name sketch">POST</div>
  <div class="step-text comic">Free post</div>
</div>

<div class="step" style="left:820px;top:730px">
  <div class="step-badge">
    <svg width="80" height="70" viewBox="0 0 80 70" fill="none" stroke="#fff" stroke-width="3" stroke-linejoin="round">
      <rect x="6" y="14" width="68" height="42" rx="3"/>
      <rect x="12" y="20" width="56" height="30" rx="2"/>
      <text x="40" y="44" text-anchor="middle" font-family="Comic Neue, cursive" font-size="22" font-weight="700" fill="#fff" stroke="none">$</text>
    </svg>
  </div>
  <div class="step-name sketch">PAID</div>
  <div class="step-text comic">Payment into your bank<br>account within two days</div>
</div>

<div class="divider" style="top:1052px"></div>

<h2 class="abs center section-title sketch" style="top:1090px">Plans</h2>
<p class="abs center section-sub comic" style="top:1138px;line-height:30px">Go or have an arrow directing to the right with bullseye shaded<br>around it (you inspire us)</p>
<p class="abs center comic" style="top:1238px;font-size:20px;letter-spacing:1px">INSTANT QUOTE</p>

<div class="go-button comic">
  <svg width="22" height="26" viewBox="0 0 22 26" fill="none" stroke="#fff" stroke-width="2" style="margin-top:20px">
    <path d="M8 14 V5 a3 3 0 0 1 6 0 V14"/>
    <path d="M4 14 h14 l-2 10 h-10 z"/>
  </svg>
  <span>GO</span>
</div>

<div class="divider" style="top:1436px"></div>

<h2 class="abs center section-title sketch" style="top:1463px">FAQ</h2>

<div class="faq-panel">
  <div class="faq-item" style="left:36px;top:36px"><p class="faq-q">Tortor sapien cursus risus, non rhoncus lectus nunc?</p><p class="faq-a">Aliquam molestie, mi et imperdiet euismod, dui purus auctor tellus, et interdum lacus lectus et ante. Sed accumsan sollicitudin sapien, sit amet adipiscing turpis gravida ac.</p></div>
  <div class="faq-item" style="left:392px;top:36px"><p class="faq-q">Tortor sapien cursus risus, non rhoncus lectus nunc?</p><p class="faq-a">Aliquam molestie, mi et imperdiet euismod, dui purus auctor tellus, et interdum lacus lectus et ante. Sed accumsan sollicitudin sapien, sit amet adipiscing turpis gravida ac.</p></div>
  <div class="faq-item" style="left:748px;top:36px"><p class="faq-q">Tortor sapien cursus risus, non rhoncus lectus nunc?</p><p class="faq-a">Aliquam molestie, mi et imperdiet euismod, dui purus auctor tellus, et interdum lacus lectus et ante. Sed accumsan sollicitudin sapien, sit amet adipiscing turpis gravida ac.</p></div>
  <div class="faq-item" style="left:36px;top:230px"><p class="faq-q">Tortor sapien cursus risus, non rhoncus lectus nunc?</p><p class="faq-a">Aliquam molestie, mi et imperdiet euismod, dui purus auctor tellus, et interdum lacus lectus et ante. Sed accumsan sollicitudin sapien, sit amet adipiscing turpis gravida ac.</p></div>
  <div class="faq-item" style="left:392px;top:230px"><p class="faq-q">Tortor sapien cursus risus, non rhoncus lectus nunc?</p><p class="faq-a">Aliquam molestie, mi et imperdiet euismod, dui purus auctor tellus, et interdum lacus lectus et ante. Sed accumsan sollicitudin sapien, sit amet adipiscing turpis gravida ac.</p></div>
  <div class="faq-item" style="left:748px;top:230px"><p class="faq-q">Tortor sapien cursus risus, non rhoncus lectus nunc?</p><p class="faq-a">Aliquam molestie, mi et imperdiet euismod, dui purus auctor tellus, et interdum lacus lectus et ante. Sed accumsan sollicitudin sapien, sit amet adipiscing turpis gravida ac.</p></div>
</div>

<h2 class="abs center section-title sketch" style="top:1952px">About us</h2>
<p class="abs about-text" style="top:2027px">Vestibulum vel metus sit amet turpis bibendum tincidunt vel sit amet quam. Pellentesque habitant morbi tristique senectus et netus et malesuada fames ac turpis egestas. Nunc consequat congue nulla eu imperdiet. Donec in est erat, id malesuada turpis. Nunc a dui id turpis convallis semper. Nunc dignissim lectus vitae eros placerat euismod. Aenean lacinia sodales eros, sit amet molestie enim consectetur eget. Sed vel magna vel eros adipiscing adipiscing eu sit amet turpis.</p>
<p class="abs about-text" style="top:2123px">At vero eos et accusamus et iusto odio dignissimos ducimus qui blanditiis praesentium voluptatum deleniti atque corrupti quos dolores et quas molestias excepturi sint occaecati cupiditate non provident, similique sunt in culpa qui officia deserunt mollitia animi, id est laborum et dolorum fuga. Et harum quidem rerum facilis est et expedita distinctioNam libero tempore,<br>cum soluta nobis est eligendi optio cumque nihil impedit quo minus id quod maxime placeat facere possimus,<br>omnis voluptas assumenda est, omnis dolor repellendus.</p>

<footer class="site-footer">
  <p class="abs contact-title">CONTACT US</p>
  <p class="abs contact-line" style="top:55px">
    <svg width="9" height="10" viewBox="0 0 10 10"><path d="M2 0 L4 2 L3 4 Q4 6 6 7 L8 6 L10 8 L8 10 Q1 9 0 2 Z" fill="#fff"/></svg>
    Phone +01 5550 2187
  </p>
  <p class="abs contact-line" style="top:80px">
    <svg width="10" height="8" viewBox="0 0 10 8"><rect width="10" height="8" fill="#fff"/><path d="M0 0 L5 4 L10 0" stroke="#061334" fill="none"/></svg>
    sales@quietharbour.com
  </p>
  <p class="abs center copyright">Copyright © 2015 Company Name All Right Reserved</p>
  <span class="social-link" style="left:1011px"></span>
  <span class="social-link" style="left:1051px"></span>
  <span class="social-link" style="left:1090px"></span>
</footer>

</body>
</html>
```